Rebrand of an existing product label

We are looking for a new design / label for our body lotion. Attached is the current product label. We have this product available in Retinol, Collagen, Hyaluronic Acid, Vitamin C, and Coconut. The brand should reflect a clinical, trustworthy look. We also want to include on the label that the product contains Dead Sea Minerals. Attached is the dieline for the label for the jar and the top. This jar is the packaging that needs to be used for this project.
Updates

Target Market(s)

40+

Requirements
Must have
• Ingredient callouts on the front + benefits. Ex- Vitamin C Brightening Cream

```html
<!DOCTYPE html>
<html lang="en">
<head>
<meta charset="UTF-8">
<title>Lumera Hyaluronic – Jar Label</title>
<link href="https://fonts.googleapis.com/css2?family=Questrial&family=Montserrat:wght@500;700;800&display=swap" rel="stylesheet">
<style>
  :root {
    --paper: #ffffff;
    --ink: #111111;
    --teal: #1f9cc2;
    --teal-light: #5fcbea;
    --rule: #e6e9ec;
  }
  * { margin: 0; padding: 0; box-sizing: border-box; }
  html, body { width: 1200px; height: 927px; overflow: hidden; background: var(--paper); }
  .canvas { position: relative; width: 1200px; height: 927px; }

  .label {
    position: absolute; left: 100px; top: 180px;
    width: 1000px; height: 560px;
    background: var(--paper);
    border: 1px solid var(--rule);
    overflow: hidden;
  }

  .dots {
    position: absolute;
  }
  .dots--left {
    left: 0; top: 0; width: 190px; height: 300px;
    background: radial-gradient(ellipse at 0% 30%, rgba(95,203,234,0.75) 0%, rgba(95,203,234,0.35) 45%, rgba(95,203,234,0) 75%);
  }
  .dots--right {
    right: 0; top: 230px; width: 140px; height: 300px;
    background: radial-gradient(ellipse at 100% 55%, rgba(95,203,234,0.75) 0%, rgba(95,203,234,0.35) 45%, rgba(95,203,234,0) 75%);
  }

  .brand {
    position: absolute; left: 0; right: 0; top: 110px;
    display: flex; justify-content: center; align-items: center; gap: 14px;
    font-family: 'Questrial', sans-serif;
    font-size: 34px; letter-spacing: 1px; color: var(--ink);
  }
  .brand__dot {
    width: 30px; height: 30px; border: 2px solid var(--ink); border-radius: 50%;
  }

  .product-name {
    position: absolute; left: 0; right: 0; top: 160px;
    text-align: center;
    font-family: 'Questrial', sans-serif;
    font-size: 132px; line-height: 1; letter-spacing: 2px;
    color: var(--ink);
  }

  .benefit {
    position: absolute; left: 0; right: 0; top: 312px;
    text-align: center;
    font-family: 'Montserrat', sans-serif; font-weight: 700;
    font-size: 22px; letter-spacing: 1.5px;
    color: var(--teal);
  }
  .benefit__lead { font-weight: 500; }

  .size-badge {
    position: absolute; left: 120px; top: 388px;
    display: inline-flex; align-items: center; gap: 12px;
    padding: 10px 30px 10px 22px;
    border-radius: 30px;
    background: var(--teal); color: var(--paper);
    font-family: 'Montserrat', sans-serif; font-weight: 800;
    font-size: 22px; letter-spacing: 1.5px;
  }
  .size-badge svg { width: 14px; height: 14px; }

  .usage {
    position: absolute; left: 130px; top: 446px;
    font-family: 'Montserrat', sans-serif; font-weight: 700;
    font-size: 17px; letter-spacing: 1px; color: var(--ink);
  }
  .usage__lead { font-weight: 500; }

  .volume {
    position: absolute; right: 150px; top: 398px;
    text-align: center;
    font-family: 'Montserrat', sans-serif; color: var(--ink);
    line-height: 1.05;
  }
  .volume__imperial { font-weight: 800; font-size: 24px; letter-spacing: 1px; }
  .volume__metric { font-weight: 500; font-size: 22px; letter-spacing: 1px; }
</style>
</head>
<body>
<div class="canvas">
  <section class="label">
    <div class="dots dots--left" role="img" aria-label="Light blue halftone dot pattern"></div>
    <div class="dots dots--right" role="img" aria-label="Light blue halftone dot pattern"></div>

    <div class="brand"><span>LUMERA</span><span class="brand__dot"></span></div>

    <h1 class="product-name">HYALURONIC</h1>

    <p class="benefit"><span class="benefit__lead">FOR</span> RADIANT, SOFT &amp; HEALTHIER LOOKING SKIN</p>

    <div class="size-badge">
      <svg viewBox="0 0 14 14" aria-hidden="true"><path d="M7 0 L8.6 5.4 L14 7 L8.6 8.6 L7 14 L5.4 8.6 L0 7 L5.4 5.4 Z" fill="#111"/></svg>
      PROFESSIONAL SIZE
    </div>
    <p class="usage"><span class="usage__lead">FOR</span> FACE, NECK &amp; HANDS</p>

    <div class="volume">
      <div class="volume__imperial">16.9 FL OZ</div>
      <div class="volume__metric">(500 ML)</div>
    </div>
  </section>
</div>
</body>
</html>
```